Broschüre für Kindertagesstätte
Zielgruppe
Wir sind eine Kindertagesstätte für Kinder ab 10 Monate mit Öffnungszeiten von 06.00 Uhr bis 19.00 Uhr
Aufgabenstellung
bitte Klappflyer gestalten, Eltern-Kind-Spielgruppe bitte im Flyer extra gestalten. Bitte hervorheben, dass wir eine hauseigene Kita-Küche haben, in der täglich frisch für unsere Kinder gekocht wird.

```html
<!DOCTYPE html>
<html lang="de">
<head>
<meta charset="utf-8">
<title>Kita Klappflyer – Innenseite</title>
<link rel="stylesheet" href="https://fonts.googleapis.com/css2?family=Oswald:wght@300;400&family=Cabin:wght@400;500&display=swap">
<style>
  :root {
    --stage: #a9a9a9;
    --cream: #fdf3e1;
    --ink: #4f484c;
    --heading: #5a5358;
    --icon-tile: #7b7275;
    --orange: #d9602b;
    --divider: #8a8a8a;
    --white: #ffffff;
    --band-purple: #8e73a8;
    --band-green: #8ab43f;
    --band-yellow: #f0b23a;
    --band-blue: #1d97d4;
    --band-red: #b5332c;
  }
  * { box-sizing: border-box; margin: 0; padding: 0; }
  html, body { width: 1200px; height: 1194px; overflow: hidden; background: var(--stage); }
  .flyer {
    position: absolute; left: 15px; top: 18px; width: 1155px; height: 1158px;
    background: var(--divider);
    font-family: "Cabin", sans-serif; color: var(--ink);
  }
  .panel { position: absolute; top: 0; width: 576px; height: 1158px; background: var(--cream); }
  .panel--left { left: 0; }
  .panel--right { left: 579px; }
  .photo { position: absolute; left: 0; top: 0; width: 576px; height: 373px; }
  .photo--blocks {
    background:
      radial-gradient(ellipse at 20% 55%, #3f8f3a 0 8%, transparent 22%),
      radial-gradient(ellipse at 60% 60%, #c9452e 0 10%, transparent 30%),
      radial-gradient(ellipse at 25% 85%, #d9c23c 0 8%, transparent 24%),
      linear-gradient(160deg, #7a5a4a 0%, #cdbfb2 45%, #e6ddd3 100%);
  }
  .photo--hall {
    background:
      radial-gradient(ellipse at 50% 75%, #c98a3c 0 25%, transparent 60%),
      linear-gradient(180deg, #e7e3da 0%, #e9b64a 35%, #d99a3a 60%, #c9883a 100%);
  }
  .heading {
    position: absolute; font-family: "Oswald", sans-serif; font-weight: 400;
    font-size: 35px; line-height: 41px; color: var(--heading); letter-spacing: 0.3px;
  }
  .heading--left { left: 61px; top: 441px; }
  .heading--right { left: 59px; top: 405px; }
  .rule { position: absolute; left: 0; top: 509px; height: 5px; background: var(--orange); border-radius: 0 3px 3px 0; }
  .panel--left .rule { width: 397px; }
  .panel--right .rule { width: 338px; }
  .feature { position: absolute; left: 61px; display: flex; gap: 15px; }
  .feature__icon {
    width: 83px; height: 83px; border-radius: 15px; background: var(--icon-tile);
    display: flex; align-items: center; justify-content: center; flex: none;
  }
  .feature__text { font-size: 21px; line-height: 35px; padding-top: 0; }
  .checklist { position: absolute; left: 57px; top: 535px; list-style: none; }
  .checklist li { display: flex; align-items: center; gap: 14px; font-size: 21px; line-height: 35px; }
  .quote-box {
    position: absolute; left: 32px; top: 809px; width: 522px; height: 287px;
    background: var(--orange); border-radius: 54px 0 32px 0; color: var(--white);
  }
  .quote-box__text {
    position: absolute; left: 48px; top: 36px;
    font-family: "Oswald", sans-serif; font-weight: 400; font-size: 33px; line-height: 45px; letter-spacing: 0.4px;
  }
  .quote-box__author { position: absolute; left: 48px; top: 216px; font-size: 17px; }
  .color-band { position: absolute; left: 0; top: 1136px; width: 1155px; height: 22px; display: flex; }
  .color-band span { height: 100%; }
</style>
</head>
<body>
<div class="flyer">
  <section class="panel panel--left">
    <div class="photo photo--blocks" role="img" aria-label="Kinderhand baut einen Turm aus bunten Bausteinen"></div>
    <h2 class="heading heading--left">Das ist besonders bei uns</h2>
    <div class="rule"></div>

    <div class="feature" style="top:536px">
      <div class="feature__icon">
        <svg width="48" height="48" viewBox="0 0 48 48" fill="none" stroke="#fff" stroke-width="2.5" stroke-linecap="round"><circle cx="24" cy="24" r="20"/><path d="M24 12v12l8 6"/></svg>
      </div>
      <p class="feature__text">lange Öffnungszeiten<br>(06.00 bis 19.00 Uhr)<br>flexible Bring- und Abholzeiten</p>
    </div>

    <div class="feature" style="top:675px">
      <div class="feature__icon">
        <svg width="50" height="46" viewBox="0 0 50 46" fill="none" stroke="#fff" stroke-width="2.5" stroke-linecap="round"><rect x="3" y="7" width="44" height="36" rx="3"/><path d="M3 17h44M13 2v9M23 2v9M33 2v9M40 2v9"/></svg>
      </div>
      <p class="feature__text">ganzjährige Aufnahme<br>keine betriebsbedingten<br>Schließzeiten</p>
    </div>

    <div class="feature" style="top:809px">
      <div class="feature__icon">
        <svg width="54" height="50" viewBox="0 0 54 50" fill="none" stroke="#fff" stroke-width="2.5" stroke-linecap="round" stroke-linejoin="round"><path d="M20 8c0-4 4-4 4-7M28 8c0-4 4-4 4-7"/><path d="M10 16h34M22 12h10"/><path d="M12 20h30v20a6 6 0 0 1-6 6H18a6 6 0 0 1-6-6z"/><path d="M12 24H4M42 24h8"/></svg>
      </div>
      <p class="feature__text" style="padding-top:1px">Gesunde Ernährung von Anfang an<br>aus unserer eigenen Kita-Küche</p>
    </div>

    <div class="feature" style="top:950px">
      <div class="feature__icon">
        <svg width="50" height="44" viewBox="0 0 50 44" fill="none" stroke="#fff" stroke-width="2.5" stroke-linejoin="round"><path d="M25 41 6 22A11 11 0 0 1 25 8a11 11 0 0 1 19 14z"/></svg>
      </div>
      <p class="feature__text">große Turn- und Bewegungshalle<br>großzügige Räume für individuelle<br>Bildungschancen</p>
    </div>
  </section>

  <section class="panel panel--right">
    <div class="photo photo--hall" role="img" aria-label="Helle Turn- und Bewegungshalle mit Rutsche, Matten und Spielgeräten"></div>
    <h2 class="heading heading--right">Weitere Angebote<br>bei uns für Ihr Kind</h2>
    <div class="rule"></div>

    <ul class="checklist">
      <li><svg width="22" height="18" viewBox="0 0 22 18" fill="none" stroke="#4f484c" stroke-width="3" stroke-linecap="round" stroke-linejoin="round"><path d="M2 9l6 6L20 2"/></svg>Kindersauna</li>
      <li><svg width="22" height="18" viewBox="0 0 22 18" fill="none" stroke="#4f484c" stroke-width="3" stroke-linecap="round" stroke-linejoin="round"><path d="M2 9l6 6L20 2"/></svg>2 Außenbereiche</li>
      <li><svg width="22" height="18" viewBox="0 0 22 18" fill="none" stroke="#4f484c" stroke-width="3" stroke-linecap="round" stroke-linejoin="round"><path d="M2 9l6 6L20 2"/></svg>Logo- und Ergotherapie möglich</li>
      <li><svg width="22" height="18" viewBox="0 0 22 18" fill="none" stroke="#4f484c" stroke-width="3" stroke-linecap="round" stroke-linejoin="round"><path d="M2 9l6 6L20 2"/></svg>Turn- und Bewegungshalle</li>
      <li><svg width="22" height="18" viewBox="0 0 22 18" fill="none" stroke="#4f484c" stroke-width="3" stroke-linecap="round" stroke-linejoin="round"><path d="M2 9l6 6L20 2"/></svg>kostenfreie Schnuppertage</li>
      <li><svg width="22" height="18" viewBox="0 0 22 18" fill="none" stroke="#4f484c" stroke-width="3" stroke-linecap="round" stroke-linejoin="round"><path d="M2 9l6 6L20 2"/></svg>uvm.</li>
    </ul>

    <blockquote class="quote-box">
      <p class="quote-box__text">„Kinder brauchen Zeit, Platz<br>und Begleitung auf ihrem<br>individuellen Entwicklungsweg!“</p>
      <p class="quote-box__author">Marlene Hofstätter, Sozialpädagogin, Kita Leiterin</p>
    </blockquote>
  </section>

  <div class="color-band">
    <span style="width:223px;background:var(--band-purple)"></span>
    <span style="width:238px;background:var(--band-green)"></span>
    <span style="width:238px;background:var(--band-yellow)"></span>
    <span style="width:238px;background:var(--band-blue)"></span>
    <span style="width:218px;background:var(--band-red)"></span>
  </div>
</div>
</body>
</html>
```